Thornwell Building Company - advertisement poster

I am looking to print some canvas signs to advertise my general contracting company, Thornwell Building Company. The sign will measure 6' long x 3' high so the size should match that ratio. I already have a logo icon, which is the Letter 'A' and some trees that I would like to incorporate, see attached. I would also like the to have the following information listed:
1) phone number: 472-318-6095
2) email: thornwellbuildingcompany@mailvistra.net
3) website: thornwellbuildingcompany.com
4) Lic#5386204
5) I want to use this text: "BUILD WITH THE T-CREW!"

The ad should be relatively simple and clean. Black and Green are my company colors. I am open to creative ideas!

Target Market(s)

People looking to renovate their homes

Industry/Entity Type

Construction

Colors
59FF00
82FF00
B8FF75
E3FFCB
F4FFEA

Requirements
Must have
• Must have my company logo
Should not have
• No photos or complex graphics

```html
<!DOCTYPE html>
<html lang="en">
<head>
<meta charset="utf-8">
<title>Thornwell Building Company – Sign</title>
<link rel="stylesheet" href="https://fonts.googleapis.com/css2?family=Orbitron:wght@500;700;800;900&family=Quicksand:wght@500&display=swap">
<style>
  :root {
    --green: #6db245;
    --green-mid: #5c8c3f;
    --green-dark: #466431;
    --charcoal: #181818;
    --black: #000000;
    --white: #ffffff;
  }
  * { margin: 0; padding: 0; box-sizing: border-box; }
  html, body { width: 1200px; height: 600px; overflow: hidden; background: var(--black); }
  .sign { position: relative; width: 1200px; height: 600px; overflow: hidden; background: var(--charcoal); }
  .sign-backdrop { position: absolute; inset: 0; }
  .headline {
    position: absolute; left: 58px; color: var(--white);
    font-family: "Orbitron", sans-serif; font-weight: 900; line-height: 1;
    letter-spacing: 2px; white-space: nowrap;
  }
  .headline--build { top: 56px; font-size: 76px; }
  .headline--with { top: 148px; font-size: 76px; }
  .crew-badge {
    position: absolute; left: 36px; top: 232px; width: 485px; height: 120px;
    background: var(--black); border: 4px solid var(--green); border-radius: 20px;
  }
  .crew-badge__text {
    position: absolute; left: 24px; top: 22px;
    font-family: "Orbitron", sans-serif; font-weight: 900; font-size: 72px;
    line-height: 1; color: var(--green); letter-spacing: 3px; white-space: nowrap;
  }
  .phone {
    position: absolute; left: 58px; top: 476px;
    font-family: "Orbitron", sans-serif; font-weight: 700; font-size: 42px;
    color: var(--white); letter-spacing: 4px; line-height: 1;
  }
  .contact {
    position: absolute; left: 60px; display: flex; align-items: center; gap: 12px;
    font-family: "Quicksand", sans-serif; font-weight: 500; font-size: 17px;
    color: var(--green); letter-spacing: 1.5px; line-height: 1;
  }
  .contact--email { top: 531px; }
  .contact--web { top: 559px; }
  .contact__icon { width: 18px; height: 18px; flex: none; }
  .brand-mark {
    position: absolute; left: 787px; top: 110px; width: 200px; height: 200px;
    border-radius: 50%; background: var(--green);
  }
  .brand-name {
    position: absolute; left: 587px; width: 600px; text-align: center;
    font-family: "Orbitron", sans-serif; font-weight: 900; color: var(--white);
    line-height: 1; white-space: nowrap;
  }
  .brand-name--main { top: 362px; font-size: 62px; letter-spacing: 1px; }
  .brand-name--sub { top: 438px; font-size: 26px; letter-spacing: 9px; }
  .license {
    position: absolute; left: 587px; width: 600px; top: 528px; text-align: center;
    font-family: "Orbitron", sans-serif; font-weight: 700; font-size: 19px;
    color: var(--green); letter-spacing: 3px; line-height: 1;
  }
</style>
</head>
<body>
<main class="sign">
  <svg class="sign-backdrop" width="1200" height="600" viewBox="0 0 1200 600" aria-hidden="true">
    <polygon points="0,0 408,0 0,582" fill="var(--green-dark)"/>
    <polygon points="0,0 361,0 0,515" fill="var(--green-mid)"/>
    <polygon points="0,0 312,0 0,447" fill="var(--green)"/>
    <polygon points="717,0 1200,0 1200,600 475,600 589,447 489,447 634,247 540,249" fill="var(--black)"/>
    <polyline points="717,0 540,249 634,247 489,447 589,447 475,600" fill="none" stroke="var(--green)" stroke-width="4"/>
  </svg>

  <h1 class="headline headline--build">BUILD</h1>
  <p class="headline headline--with">WITH THE</p>
  <div class="crew-badge"><span class="crew-badge__text">T-CREW!</span></div>

  <p class="phone">472-318-6095</p>
  <p class="contact contact--email">
    <svg class="contact__icon" viewBox="0 0 18 18" aria-hidden="true"><rect x="1.5" y="3.5" width="15" height="11" rx="2" fill="none" stroke="var(--green)" stroke-width="2"/><polyline points="2,5 9,10 16,5" fill="none" stroke="var(--green)" stroke-width="2"/></svg>
    thornwellbuildingcompany@mailvistra.net
  </p>
  <p class="contact contact--web">
    <svg class="contact__icon" viewBox="0 0 18 18" aria-hidden="true"><circle cx="9" cy="9" r="7.5" fill="none" stroke="var(--green)" stroke-width="1.8"/><ellipse cx="9" cy="9" rx="3.2" ry="7.5" fill="none" stroke="var(--green)" stroke-width="1.5"/><line x1="1.5" y1="9" x2="16.5" y2="9" stroke="var(--green)" stroke-width="1.5"/><line x1="3" y1="5" x2="15" y2="5" stroke="var(--green)" stroke-width="1.3"/><line x1="3" y1="13" x2="15" y2="13" stroke="var(--green)" stroke-width="1.3"/></svg>
    thornwellbuildingcompany.com
  </p>

  <div class="brand-mark" aria-hidden="true"></div>
  <p class="brand-name brand-name--main">THORNWELL</p>
  <p class="brand-name brand-name--sub">BUILDING COMPANY</p>
  <p class="license">LICENSE# 5386204</p>
</main>
</body>
</html>
```